Commercial Rooftop Solar business needs a website

We need a website with fantastic appeal for a new company based in Melbourne called Brightvale Energy. We design and install solar energy systems for commercial applications across Australia. Our market is to focus on small to medium businesses looking for solar solutions, but we will also provide our service for residential customers. We would like a beautiful 'front page' feel to our home page, using photographs of solar PV systems and/or natural imagery. Our logo uses the colours orange and black, which could easily be echoed in photographic imagery of sunset and sunrise, for example. The design should communicate quiet confidence and professionalism to a corporate marketplace.

NEW POINTS FOR BRIEF: This design also needs to be flexible to allow for additional future content, including a Support page with sub pages, FAQ's, and a Blog.

As part of this design project, we will require the coding for the website to be completed by the designer.

We have seen some websites, which we like the look and feel of: these are listed below.

keenroofpower.com.au:

• Beautiful images underlaying brief text selling points.
• Simple ‘front cover’ style home page with elegant drop-down menu, stylish simple font style.
• Home page invites exploration through the menu links, rather than trying to provide all the information up front.
• Company logo and name in the top left hand corner, contact details accessible at top right hand, seems consistent in most sites.

tolvaenergy.com.au

brinkeltpower.com:
• Same element as the others is the front-page style home page with beautiful images underlying text.

We have a webpage that we started uploading content to. You can use some of the content there in your designs: www.brightvaleenergy.com.au

Technical Specifications:
PAGES:

Home

About Us

Solutions - Commercial
- Residential

Products - Solar Panels - Morvo Falcon, Morvo CELT, Morvo KT
- Solar Inverters - Valtrex, SunPivot
- Monitoring systems - Lumen Metrics
- Batteries - QD

- Datasheets have been provided for reference but if it's too much work, you can use generic text and we will provide content later.

Contact Us

FUTURE PAGES (Please consider in structure, where links could be placed):

Support

FAQ's

Blog.

We could provide some content for the Support page soon, but the Blog and FAQ's are future pages which we don't want highlighted in the design as we don't yet have content.

Phone: 1800 7 VOLTA
Email: sales@brightvaleenergy.com.au

Currently, I do not have images and text available. Please
use placeholders in the meantime. The final text and images will be uploaded for the winner once a winning design has been selected.

Target Market(s)

Primary focus is on small to medium sized business owners. Those owners will have a house which may be suitable for solar so we want to cater to residential deeper in the website.

Industry/Entity Type

Solar Energy

Coding

Coded - Design and coding required

Number of Pages Required

5+ page

Colors
f78f20
0255a3

Requirements
Must have
• Logo as per attachments.
Nice to have
• Logo can have alternate colours Eg. White on Orange or Black etc. provided colour correct logo is shown somewhere eg. footer or contact page.
• In the active site, I'd like to have:
• Very slowly zooming images - barely perceptible.
• Title text that rolls into place
• Subtle movements
• See https://paylarkfinance.com.au/ for example

```html
<!DOCTYPE html>
<html lang="en">
<head>
<meta charset="utf-8">
<title>Brightvale Energy – Commercial Solar Solutions</title>
<link href="https://fonts.googleapis.com/css2?family=Raleway:wght@500;600;700;800&family=Open+Sans:wght@400;600;700&display=swap" rel="stylesheet">
<style>
:root{
  --orange:#f78f20;
  --orange-dark:#e07a10;
  --blue:#0255a3;
  --blue-dark:#0a4a8c;
  --ink:#222;
  --text:#444;
  --muted:#777;
  --light:#f1f1f1;
  --footer:#2b2b2b;
  --white:#fff;
}
*{box-sizing:border-box;margin:0;padding:0}
html,body{width:1200px;height:3488px;overflow:hidden}
body{position:relative;font-family:"Open Sans",Arial,sans-serif;color:var(--text);background:var(--white)}
.abs{position:absolute}
a{color:inherit;text-decoration:none}

/* header + hero */
.hero{left:0;top:0;width:1200px;height:605px;
  background:
    radial-gradient(ellipse 520px 260px at 780px 330px,rgba(18,34,80,.95) 0%,rgba(28,52,110,.85) 45%,rgba(28,52,110,0) 100%),
    radial-gradient(ellipse 260px 150px at 90px 420px,rgba(22,40,92,.9) 0%,rgba(22,40,92,0) 100%),
    radial-gradient(ellipse 300px 120px at 980px 250px,rgba(255,255,255,.75) 0%,rgba(255,255,255,0) 100%),
    radial-gradient(ellipse 260px 110px at 380px 230px,rgba(255,255,255,.6) 0%,rgba(255,255,255,0) 100%),
    linear-gradient(180deg,#2a62a8 0%,#5a92cc 28%,#bcd3e8 50%,#6aa04a 62%,#5b9a3c 78%,#3b6b28 100%)}
.brand{left:80px;top:28px;color:var(--white);font-family:"Raleway",sans-serif;font-weight:700;font-size:30px;letter-spacing:1px;display:flex;align-items:center;gap:12px}
.brand .dot{width:40px;height:40px;border-radius:50%;background:var(--white)}
.topbar{right:80px;top:20px;display:flex;align-items:center;gap:26px;color:var(--white);font-family:"Raleway",sans-serif;font-weight:700;font-size:19px}
.topbar .phone{display:flex;align-items:center;gap:10px}
.btn-estimate{background:var(--orange);color:var(--white);border-radius:22px;padding:8px 54px 8px 24px;font-size:14px;letter-spacing:.5px;position:relative}
.btn-estimate svg{position:absolute;right:18px;top:7px}
.nav{right:80px;top:90px;display:flex;gap:80px;color:var(--white);font-family:"Raleway",sans-serif;font-weight:700;font-size:17px}
.hero-title{left:0;width:1200px;top:498px;text-align:center;color:var(--white);font-family:"Raleway",sans-serif;font-weight:700;font-size:32px;line-height:48px;text-shadow:0 2px 6px rgba(0,0,0,.45)}
.arrow{top:530px;color:var(--white)}

/* services */
.service{top:605px;width:600px;height:176px;display:flex;align-items:flex-start;gap:28px;padding:38px 0 0 80px;color:var(--white)}
.service.commercial{left:0;background:var(--blue)}
.service.residential{left:600px;background:var(--orange);padding-left:26px}
.service .badge{flex:none;width:118px;height:118px;border-radius:50%;border:5px solid var(--white);display:flex;align-items:center;justify-content:center;margin-top:-4px}
.commercial .badge{background:var(--orange)}
.residential .badge{background:var(--blue)}
.service h3{font-family:"Raleway",sans-serif;font-weight:700;font-size:24px;margin:4px 0 10px}
.service p{font-size:13px;line-height:21px;max-width:420px}
.service p b{color:var(--white)}

/* section titles */
.section-title{left:0;width:1200px;text-align:center;font-family:"Raleway",sans-serif;font-weight:800;font-size:32px;color:var(--blue);letter-spacing:.5px;display:flex;justify-content:center;align-items:center;gap:22px}
.section-title::before,.section-title::after{content:"";width:140px;height:2px;background:var(--blue)}
.section-title .accent{color:var(--orange)}

/* about */
.about-text{left:95px;width:1010px;top:882px;text-align:center;font-size:14px;line-height:24px;color:var(--text)}
.about-text p+p{margin-top:10px}
.btn{background:var(--orange);color:var(--white);font-family:"Raleway",sans-serif;font-weight:700;border-radius:24px;text-align:center}
.btn-read{left:520px;top:1014px;width:160px;height:42px;line-height:42px;font-size:16px}

/* stats */
.stats{left:0;top:1105px;width:1200px;height:302px;
  background:
    radial-gradient(ellipse 260px 200px at 960px 60px,rgba(200,205,210,.55) 0%,rgba(200,205,210,0) 100%),
    radial-gradient(ellipse 400px 220px at 150px 250px,rgba(40,70,120,.8) 0%,rgba(40,70,120,0) 100%),
    linear-gradient(135deg,#1f2a38 0%,#3a4a5c 45%,#2a3340 100%)}
.stat{top:1163px;width:249px;height:209px;background:#111;color:var(--white);text-align:center;padding-top:20px}
.stat .num{font-family:"Raleway",sans-serif;font-weight:700;font-size:32px;margin-top:10px}
.stat p{font-size:12px;line-height:18px;margin:8px 22px 0}

/* products */
.products-bg{left:0;top:1407px;width:1200px;height:500px;background:var(--light)}
.product{top:1516px;width:388px;height:391px;border:2px solid #555;background:var(--white);overflow:hidden}
.product .media{top:24px;height:300px}
.product .label{left:-2px;top:270px;width:340px;height:76px;border-radius:0 40px 40px 0;color:var(--white);font-family:"Raleway",sans-serif;font-weight:700;font-size:24px;line-height:76px;padding-left:20px;box-shadow:4px 6px 6px rgba(0,0,0,.35)}
.label.blue{background:var(--blue)}
.label.orange{background:var(--orange)}

/* why choose */
.why-bg{left:0;top:1953px;width:1200px;height:674px;background:linear-gradient(180deg,#ffffff 0%,#eceff2 50%,#dfe4e9 100%)}
.feature-icon{width:86px;height:86px;border-radius:50%;background:var(--orange);border:4px solid #fbd3a6;display:flex;align-items:center;justify-content:center}
.feature-label{font-size:16px;line-height:24px;color:var(--ink)}
.feature-label.left{text-align:right;width:220px}
.core-name{left:460px;top:2290px;width:280px;text-align:center;font-family:"Raleway",sans-serif;font-weight:800;font-size:28px;color:var(--orange)}

/* promise */
.promise{left:0;top:2627px;width:1200px;height:396px;
  background:
    radial-gradient(ellipse 420px 300px at 200px 180px,rgba(255,236,190,.95) 0%,rgba(255,236,190,0) 100%),
    radial-gradient(ellipse 500px 160px at 800px 360px,rgba(120,130,50,.9) 0%,rgba(120,130,50,0) 100%),
    linear-gradient(100deg,#f3d9a0 0%,#f1b95a 30%,#b8a05c 60%,#7b8a3f 100%)}
.ribbon{left:570px;top:2762px;width:630px;height:133px;background:rgba(247,143,32,.92);border-radius:66px 0 0 66px;color:var(--white);font-family:"Raleway",sans-serif;font-weight:700;font-size:25px;line-height:33px;text-align:center;padding-top:17px}

/* referral */
.referral{left:0;top:3023px;width:1200px;height:70px;background:#111;color:var(--white)}
.referral .text{left:100px;top:19px;font-size:23px;white-space:nowrap}
.btn-more{left:866px;top:17px;width:222px;height:38px;line-height:38px;font-size:16px}

/* footer */
.footer{left:0;top:3093px;width:1200px;height:343px;background:var(--footer);color:var(--white)}
.footer h4{font-family:"Raleway",sans-serif;font-weight:700;font-size:19px;letter-spacing:.5px}
.quick li{list-style:none;font-size:15px;margin-bottom:26px;display:flex;gap:18px}
.contact li{list-style:none;display:flex;gap:14px;font-size:15px;line-height:21px;margin-bottom:24px}
.contact .ci{flex:none;width:32px;height:32px;border-radius:50%;border:2px solid var(--orange);display:flex;align-items:center;justify-content:center}
.map{left:614px;top:3187px;width:254px;height:152px;border:3px solid #ccc;background:linear-gradient(135deg,#e7eadf 0%,#d9ddcf 100%)}
.social{display:flex;gap:14px}
.social span{width:42px;height:42px;border-radius:50%;background:var(--orange);display:block}
.footer-name{left:952px;top:3270px;width:180px;text-align:center;font-family:"Raleway",sans-serif;font-weight:800;font-size:26px;color:var(--orange);line-height:32px}
.copy{left:0;top:3436px;width:1200px;height:52px;background:var(--orange);color:var(--white);font-size:13px;text-align:center;line-height:52px}
</style>
</head>
<body>

<!-- Hero -->
<section class="hero abs" role="img" aria-label="Photograph of ground-mounted solar panels on green grass under a blue cloudy sky"></section>
<div class="brand abs"><span class="dot"></span>BRIGHTVALE ENERGY</div>
<div class="topbar abs">
  <div class="phone">
    <svg width="30" height="30" viewBox="0 0 30 30"><circle cx="15" cy="15" r="13" fill="none" stroke="#fff" stroke-width="2"/><path d="M10 9c1-1 2-1 3 0l1 2c0 1-1 2-1 2 1 2 2 3 4 4 0 0 1-1 2-1l2 1c1 1 1 2 0 3-2 2-5 1-8-2s-4-6-3-9z" fill="#fff"/></svg>
    1800 7 VOLTA
  </div>
  <a class="btn-estimate" href="#">FREE ESTIMATE
    <svg width="20" height="20" viewBox="0 0 20 20"><rect x="2" y="2" width="14" height="16" fill="none" stroke="#fff" stroke-width="1.6"/><path d="M6 14l9-10 2 2-9 10H6z" fill="#fff"/></svg>
  </a>
</div>
<nav class="nav abs"><a href="#">HOME</a><a href="#">ABOUT US</a><a href="#">SOLUTIONS</a><a href="#">CONTACT US</a></nav>
<h1 class="hero-title abs">Brightvale Energy Is A National Company That Specialises<br>In Solar Solutions For The Commercial Market</h1>
<svg class="arrow abs" style="left:22px" width="20" height="32" viewBox="0 0 20 32"><path d="M16 3L4 16l12 13" fill="none" stroke="#fff" stroke-width="3"/></svg>
<svg class="arrow abs" style="left:1158px" width="20" height="32" viewBox="0 0 20 32"><path d="M4 3l12 13L4 29" fill="none" stroke="#fff" stroke-width="3"/></svg>

<!-- Services -->
<div class="service commercial abs">
  <div class="badge"><svg width="50" height="50" viewBox="0 0 50 50" fill="#fff"><rect x="8" y="10" width="22" height="34"/><rect x="30" y="20" width="12" height="24"/><g fill="#f78f20"><rect x="12" y="14" width="5" height="5"/><rect x="21" y="14" width="5" height="5"/><rect x="12" y="23" width="5" height="5"/><rect x="21" y="23" width="5" height="5"/><rect x="12" y="32" width="5" height="5"/><rect x="21" y="32" width="5" height="5"/><rect x="34" y="25" width="4" height="4"/><rect x="34" y="33" width="4" height="4"/></g></svg></div>
  <div><h3>COMMERCIAL SERVICES</h3><p>Lorem ipsum dolor sit amet, consectetuer adipiscing elit, seddiam nonummy nibh euismod tincidunt ut laoreetfgf doloremagna aliquam erat volutpat....<b>[+]</b></p></div>
</div>
<div class="service residential abs">
  <div class="badge"><svg width="54" height="50" viewBox="0 0 54 50" fill="#fff"><path d="M27 6L4 26h7v18h32V26h7z"/><rect x="22" y="30" width="10" height="14" fill="#0255a3"/><rect x="14" y="29" width="6" height="6" fill="#0255a3"/><rect x="34" y="29" width="6" height="6" fill="#0255a3"/></svg></div>
  <div><h3>RESIDENTIAL SERVICES</h3><p>Lorem ipsum dolor sit amet, consectetuer adipiscing elit, seddiam nonummy nibh euismod tincidunt ut laoreetfgf doloremagna aliquam erat volutpat....<b style="color:#0255a3">[+]</b></p></div>
</div>

<!-- About -->
<h2 class="section-title abs" style="top:820px"><span>ABOUT <span class="accent">BRIGHTVALE ENERGY</span></span></h2>
<div class="about-text abs">
  <p>Brightvale Energy is a national company that specialises in solar solutions for the commercial market. We also provide solutions for the residential market, bringing our uncompromising quality and service to the home.</p>
  <p>The founder of the company has over 10 years experience delivering projects on both a residential and commercial scale, having overseen the installation of more than 3 megawatts of solar projects. They were a pioneer on the first megawatt scale project in Australia.</p>
</div>
<a class="btn btn-read abs" href="#">READ MORE</a>

<!-- Stats -->
<section class="stats abs" role="img" aria-label="Dark photograph of a technician working on solar panels"></section>
<div class="stat abs" style="left:81px">
  <svg width="44" height="44" viewBox="0 0 44 44" fill="none" stroke="#fff" stroke-width="2.5"><path d="M10 4v36M22 4v36M34 4v36"/><rect x="6" y="12" width="8" height="6" fill="#111"/><rect x="18" y="24" width="8" height="6" fill="#111"/><rect x="30" y="10" width="8" height="6" fill="#111"/></svg>
  <div class="num">72%</div><p>Amount Electricity prices rose in five years until June 2012</p>
</div>
<div class="stat abs" style="left:344px">
  <svg width="44" height="44" viewBox="0 0 44 44" fill="none" stroke="#fff" stroke-width="2.5"><rect x="6" y="4" width="32" height="36"/><rect x="11" y="10" width="10" height="9"/><path d="M25 11h8M25 17h8M11 25h22M11 31h22"/></svg>
  <div class="num">29%</div><p>The predicted amount electricity prices will rise by 2020</p>
</div>
<div class="stat abs" style="left:609px">
  <svg width="60" height="44" viewBox="0 0 60 44" fill="none" stroke="#fff" stroke-width="2.5"><path d="M4 12h48v26H4z"/><path d="M10 6h46v26"/><text x="22" y="32" fill="#fff" stroke="none" font-size="16" font-family="Open Sans,sans-serif">$</text></svg>
  <div class="num">$19Billion</div><p>has been invested into renewable energy in Australia since 2001</p>
</div>
<div class="stat abs" style="left:872px">
  <svg width="44" height="44" viewBox="0 0 44 44" fill="none" stroke="#fff" stroke-width="2.5"><path d="M22 4a12 12 0 0 0-7 22v6h14v-6a12 12 0 0 0-7-22z"/><path d="M16 36h12M18 40h8"/></svg>
  <div class="num">2320MW</div><p>RECORDED SOLAR Photovoltaic INSTALLED IN AUSTRALIA in 2012</p>
</div>

<!-- Products -->
<div class="products-bg abs"></div>
<h2 class="section-title abs" style="top:1440px"><span>OUR <span class="accent">PRODUCTS</span></span></h2>
<div class="product abs" style="left:0">
  <div class="media abs" role="img" aria-label="Photograph of a single blue solar panel" style="left:100px;width:180px;background:linear-gradient(160deg,#3a5290 0%,#22346a 45%,#1a2850 100%)"></div>
  <div class="label blue abs">SOLAR PANELS</div>
</div>
<div class="product abs" style="left:407px">
  <div class="media abs" role="img" aria-label="Photograph of solar inverter units with a small panel" style="left:10px;width:364px;background:radial-gradient(ellipse 140px 60px at 120px 40px,#2c4478 0%,rgba(44,68,120,0) 100%),radial-gradient(ellipse 70px 110px at 260px 170px,#c9ced3 0%,rgba(201,206,211,0) 100%),radial-gradient(ellipse 80px 90px at 120px 200px,#d6dadd 0%,rgba(214,218,221,0) 100%),linear-gradient(180deg,#f4f5f6,#e6e8ea)"></div>
  <div class="label orange abs">SOLAR INVERTERS</div>
</div>
<div class="product abs" style="left:811px">
  <div class="media abs" role="img" aria-label="Photograph of a monitoring dashboard on a desktop screen and phone" style="left:20px;width:344px;background:radial-gradient(ellipse 150px 90px at 140px 110px,#d5dae2 0%,rgba(213,218,226,0) 100%),radial-gradient(ellipse 30px 60px at 310px 160px,#3a3d45 0%,rgba(58,61,69,0) 100%),linear-gradient(180deg,#f1f3f6,#e3e7ec)"></div>
  <div class="label blue abs">MONITORING SYSTEMS</div>
</div>

<!-- Why choose -->
<div class="why-bg abs" role="img" aria-label="Faint photograph of solar panel cells"></div>
<h2 class="section-title abs" style="top:2006px"><span>WHY CHOOSE <span class="accent">BRIGHTVALE</span> ENERGY</span></h2>
<svg class="abs" style="left:0;top:1953px" width="1200" height="674" viewBox="0 1953 1200 674">
  <circle cx="600" cy="2325" r="186" fill="#fff" fill-opacity=".5" stroke="#555" stroke-width="2"/>
  <g fill="none" stroke="#555" stroke-width="2" stroke-dasharray="4 5">
    <path d="M392 2158h45l45 40"/><path d="M392 2325h90"/><path d="M392 2493h45l45-40"/>
    <path d="M808 2158h-45l-45 40"/><path d="M808 2325h-90"/><path d="M808 2493h-45l-45-40"/>
  </g>
  <g fill="#0255a3"><circle cx="482" cy="2198" r="6"/><circle cx="482" cy="2325" r="6"/><circle cx="482" cy="2453" r="6"/><circle cx="718" cy="2198" r="6"/><circle cx="718" cy="2325" r="6"/><circle cx="718" cy="2453" r="6"/></g>
</svg>
<div class="core-name abs">BRIGHTVALE<br>ENERGY</div>

<div class="feature-icon abs" style="left:306px;top:2115px"><svg width="34" height="40" viewBox="0 0 34 40" fill="#fff"><path d="M17 2a13 13 0 0 0-13 13c0 10 13 23 13 23s13-13 13-23A13 13 0 0 0 17 2zm0 18a5 5 0 1 1 0-10 5 5 0 0 1 0 10z"/></svg></div>
<div class="feature-label left abs" style="left:72px;top:2135px">100% Locally<br>Owned &amp; Operated</div>
<div class="feature-icon abs" style="left:306px;top:2282px"><svg width="40" height="40" viewBox="0 0 40 40" fill="none" stroke="#fff" stroke-width="2.5"><circle cx="20" cy="16" r="11"/><circle cx="20" cy="16" r="5"/><path d="M13 25l-3 12 10-5 10 5-3-12"/></svg></div>
<div class="feature-label left abs" style="left:72px;top:2302px">Top Quality<br>Components</div>
<div class="feature-icon abs" style="left:306px;top:2450px"><svg width="44" height="40" viewBox="0 0 44 40" fill="#fff"><path d="M22 4l3 6 6 1-4 4 1 6-6-3-6 3 1-6-4-4 6-1z"/><path d="M9 20l2 4 4 .5-3 3 .8 4L9 29.5 5.2 31.5 6 27.5l-3-3 4-.5zM35 20l2 4 4 .5-3 3 .8 4-3.8-2-3.8 2 .8-4-3-3 4-.5z"/></svg></div>
<div class="feature-label left abs" style="left:72px;top:2470px">Ranked Top Solar<br>Contractor Nationally</div>

<div class="feature-icon abs" style="left:802px;top:2115px"><svg width="40" height="40" viewBox="0 0 40 40" fill="none" stroke="#fff" stroke-width="2.5"><circle cx="20" cy="18" r="12"/><circle cx="20" cy="18" r="5" fill="#fff"/><path d="M14 29l-2 8 8-4 8 4-2-8"/></svg></div>
<div class="feature-label abs" style="left:912px;top:2147px">Top Quality Components</div>
<div class="feature-icon abs" style="left:802px;top:2282px"><svg width="40" height="40" viewBox="0 0 40 40" fill="none" stroke="#fff" stroke-width="2.5"><circle cx="20" cy="20" r="7"/><path d="M20 3v6M20 31v6M3 20h6M31 20h6M8 8l4 4M28 28l4 4M8 32l4-4M28 12l4-4"/></svg></div>
<div class="feature-label abs" style="left:912px;top:2302px">Over 3,000 Installations<br>In New England</div>
<div class="feature-icon abs" style="left:802px;top:2450px"><svg width="40" height="40" viewBox="0 0 40 40" fill="none" stroke="#fff" stroke-width="2.5"><path d="M20 6a10 10 0 0 0-6 18v5h12v-5a10 10 0 0 0-6-18z"/><path d="M16 33h8M4 16h4M32 16h4M8 5l3 3M32 5l-3 3"/></svg></div>
<div class="feature-label abs" style="left:912px;top:2486px">Vertically Integrated</div>

<!-- Promise -->
<section class="promise abs" role="img" aria-label="Warm sunset photograph of a mother and child in a grassy field"></section>
<div class="ribbon abs">We Go the Extra Mile to Support Our<br>Customers and They Have Made Us the<br>#1 Residential Solar Installer in the State.</div>

<!-- Referral -->
<div class="referral abs">
  <div class="text abs">Help a Friend Go Solar. Ask About Our Referral Program.</div>
  <svg class="abs" style="left:800px;top:27px" width="52" height="18" viewBox="0 0 52 18"><path d="M2 12c14-6 30-6 46-2" fill="none" stroke="#fff" stroke-width="2"/><path d="M42 5l7 5-8 3" fill="none" stroke="#fff" stroke-width="2"/></svg>
  <a class="btn btn-more abs" href="#">MORE INFORMATION</a>
</div>

<!-- Footer -->
<footer class="footer abs">
  <h4 class="abs" style="left:80px;top:58px">QUICK LINKS</h4>
  <ul class="quick abs" style="left:80px;top:114px">
    <li><span>›</span>Home</li><li><span>›</span>About Us</li><li><span>›</span>Solutions</li><li><span>›</span>Contact Us</li>
  </ul>
  <h4 class="abs" style="left:318px;top:58px">CONTACT DETAILS</h4>
  <ul class="contact abs" style="left:322px;top:108px;width:260px">
    <li><span class="ci"><svg width="14" height="16" viewBox="0 0 14 16" fill="#f78f20"><path d="M7 0a6 6 0 0 0-6 6c0 4 6 10 6 10s6-6 6-10a6 6 0 0 0-6-6zm0 8a2 2 0 1 1 0-4 2 2 0 0 1 0 4z"/></svg></span><span>BRIGHTVALE ENERGY<br>123 ipsum dolor sit amet,<br>consectetuer adipiscing</span></li>
    <li><span class="ci"><svg width="16" height="16" viewBox="0 0 16 16" fill="#f78f20"><path d="M3 1c1-1 2-1 3 0l1 3c0 1-1 2-1 2 1 2 2 3 4 4 0 0 1-1 2-1l3 1c1 1 1 2 0 3-2 2-5 1-8-2S2 4 3 1z"/></svg></span><span style="line-height:32px">1800 7 VOLTA</span></li>
    <li><span class="ci"><svg width="16" height="12" viewBox="0 0 16 12" fill="none" stroke="#f78f20" stroke-width="1.6"><rect x="1" y="1" width="14" height="10"/><path d="M1 1l7 6 7-6"/></svg></span><span style="line-height:32px;font-size:13px">info@brightvaleenergy.com.au</span></li>
  </ul>
  <h4 class="abs" style="left:610px;top:58px">LOCATION MAP</h4>
  <h4 class="abs" style="left:914px;top:58px">FOLLOW US</h4>
  <div class="social abs" style="left:914px;top:108px" aria-label="Social media links"><span></span><span></span><span></span><span></span></div>
</footer>
<div class="map abs" role="img" aria-label="Location map of the office"></div>
<div class="footer-name abs">BRIGHTVALE<br>ENERGY</div>
<div class="copy abs">© 2017 BRIGHTVALE ENERGY . All rights reserved &nbsp; | &nbsp; Privacy Policy</div>

</body>
</html>
```